Food supplement packaging for functional chewing

We need a design of 2 boxes of a food supplement in functional chewing gum for Immune system enhancement and a multivitamin complex. Both products can be used by adults and children above 7. Products will be sold online.
More information in attached. PDF of similar product with dimensions of the box and the company logo also in attached. We would like that the design follows somehow the graphics of the existing product.

Target Market(s)

Families that seek health

Industry/Entity Type

Pharmaceuticals

Requirements
Nice to have
• vivid colours

```html
<!DOCTYPE html>
<html lang="it">
<head>
<meta charset="utf-8">
<title>Vitaguard Gums – packaging front</title>
<link rel="stylesheet" href="https://fonts.googleapis.com/css2?family=Archivo:ital,wght@0,700;0,800;1,400;1,700;1,800;1,900&display=swap">
<style>
  :root {
    --red-deep: #c1272d;
    --red-mid: #d8322f;
    --orange: #f05a28;
    --pink: #e6a2a4;
    --pink-soft: #f5bcbd;
    --blue-glow: #cfe9fa;
    --blue-shield: #1f7ae0;
    --ink: #111111;
    --white: #ffffff;
    --grey: #c9c9c9;
  }
  * { margin: 0; padding: 0; box-sizing: border-box; }
  html, body { width: 1200px; height: 546px; overflow: hidden; background: var(--white); }
  body { font-family: "Archivo", Arial, sans-serif; }
  .pack { position: relative; width: 1200px; height: 546px; overflow: hidden; }
  .pack-art { position: absolute; inset: 0; width: 1200px; height: 546px; }

  .hero-visual {
    position: absolute; left: 86px; top: 59px; width: 250px; height: 250px; border-radius: 50%;
    background: radial-gradient(circle at 50% 50%, var(--blue-shield) 0 22%, #8cc8f2 34%, var(--blue-glow) 52%, rgba(207,233,250,0) 72%);
  }

  .claim { position: absolute; left: 469px; top: 66px; color: var(--ink); }
  .claim-intro { font-style: italic; font-weight: 400; font-size: 15.5px; }
  .claim-ingredients { font-style: italic; font-weight: 800; font-size: 15.5px; margin-top: 9px; padding-left: 3px; }

  .product-name { position: absolute; left: 106px; top: 328px; font-style: italic; font-weight: 900; font-size: 47px; line-height: 1.02; letter-spacing: -0.5px; }
  .product-name .line-brand { display: block; color: var(--red-mid); }
  .product-name .line-type { display: block; color: var(--ink); }

  .free-badges { position: absolute; left: 1046px; top: 72px; width: 74px; list-style: none; }
  .free-badge { display: flex; flex-direction: column; align-items: center; height: 105px; }
  .free-badge svg { width: 56px; height: 56px; }
  .free-badge span { margin-top: 6px; color: var(--white); font-weight: 800; font-size: 9.5px; white-space: nowrap; }

  .pack-footer { position: absolute; right: 23px; top: 435px; text-align: right; color: var(--white); font-style: italic; font-weight: 700; font-size: 15.5px; line-height: 1.3; }
</style>
</head>
<body>
<main class="pack">
  <svg class="pack-art" viewBox="0 0 1535 697" preserveAspectRatio="none" aria-hidden="true">
    <defs>
      <linearGradient id="panelRed" x1="0.3" y1="1" x2="1" y2="0.2">
        <stop offset="0" stop-color="#f05a28"/>
        <stop offset="0.45" stop-color="#e0402b"/>
        <stop offset="1" stop-color="#c1272d"/>
      </linearGradient>
      <linearGradient id="swooshGrey" x1="0" y1="1" x2="1" y2="0">
        <stop offset="0" stop-color="#ffffff"/>
        <stop offset="0.5" stop-color="#d4d4d4"/>
        <stop offset="1" stop-color="#b5b5b5"/>
      </linearGradient>
      <clipPath id="cardClip"><rect x="40" y="20" width="1480" height="648"/></clipPath>
    </defs>
    <g clip-path="url(#cardClip)">
      <ellipse cx="850" cy="90" rx="460" ry="205" fill="#e6a2a4" opacity="0.7"/>
      <path d="M1270 20 L1520 20 L1520 668 L40 668 C640 640 1110 520 1215 250 C1250 160 1262 90 1270 20 Z" fill="url(#panelRed)"/>
      <path d="M1140 20 C1030 150 980 300 968 440 C1060 390 1150 320 1200 240 C1230 160 1230 90 1210 20 Z" fill="#f5bcbd" opacity="0.75"/>
      <ellipse cx="850" cy="90" rx="460" ry="205" fill="#e6a2a4" opacity="0.35"/>
      <path d="M1190 20 C1280 250 1080 560 40 668 C760 620 1240 420 1272 20 Z" fill="url(#swooshGrey)"/>
      <path d="M1182 20 C1262 260 1060 570 40 668 C740 610 1225 420 1246 20 Z" fill="#ffffff"/>
    </g>
  </svg>

  <div class="hero-visual" role="img" aria-label="Illustrazione: scudo blu protettivo circondato da virus rossi"></div>

  <div class="claim">
    <p class="claim-intro">Integratore alimentare in chewing gum con</p>
    <p class="claim-ingredients">Echinacea, Uncaria, Sambucco, Vitamine e Minerali</p>
  </div>

  <h1 class="product-name">
    <span class="line-brand">Vitaguard</span>
    <span class="line-type">Gums</span>
  </h1>

  <ul class="free-badges">
    <li class="free-badge">
      <svg viewBox="0 0 56 56" aria-hidden="true">
        <circle cx="28" cy="28" r="25" fill="none" stroke="#fff" stroke-width="5"/>
        <path d="M17 24 L27 19 L37 24 L37 36 L27 41 L17 36 Z M17 24 L27 29 L37 24 M27 29 L27 41" fill="#fff" stroke="#d8322f" stroke-width="1.5"/>
        <line x1="11" y1="45" x2="45" y2="11" stroke="#fff" stroke-width="5"/>
      </svg>
      <span>SUGAR FREE</span>
    </li>
    <li class="free-badge">
      <svg viewBox="0 0 56 56" aria-hidden="true">
        <circle cx="28" cy="28" r="25" fill="none" stroke="#fff" stroke-width="5"/>
        <path d="M28 13 C32 18 32 22 28 26 C24 22 24 18 28 13 Z" fill="#fff"/>
        <path d="M27 28 C22 28 18 25 17 20 C22 20 26 23 27 28 Z M29 28 C34 28 38 25 39 20 C34 20 30 23 29 28 Z" fill="#fff"/>
        <path d="M27 36 C22 36 18 33 17 28 C22 28 26 31 27 36 Z M29 36 C34 36 38 33 39 28 C34 28 30 31 29 36 Z" fill="#fff"/>
        <rect x="27" y="26" width="2" height="17" fill="#fff"/>
        <line x1="11" y1="45" x2="45" y2="11" stroke="#fff" stroke-width="5"/>
      </svg>
      <span>GLUTEN FREE</span>
    </li>
    <li class="free-badge">
      <svg viewBox="0 0 56 56" aria-hidden="true">
        <circle cx="28" cy="28" r="25" fill="none" stroke="#fff" stroke-width="5"/>
        <path d="M28 13 C33 21 38 27 38 33 A10 10 0 0 1 18 33 C18 27 23 21 28 13 Z" fill="#fff"/>
        <line x1="11" y1="45" x2="45" y2="11" stroke="#fff" stroke-width="5"/>
      </svg>
      <span>LACTOSE FREE</span>
    </li>
  </ul>

  <footer class="pack-footer">
    <p>PER LE NATURALI DIFERSE DEL ORGANISMO</p>
    <p>10 chewing gum da 2,2 g</p>
  </footer>
</main>
</body>
</html>
```